Billboard for Lawyers who handle work accident cases

We need a billboard design for our law firm based in Queens, New York. The billboard is 8 by 10. The billboard is long and not wide.

Our firm focuses on work accidents. We are looking for a professional ad that will catch the attention of drivers and pedestrians passing by. The ad should be to the point.

I am attaching our picture and our logo for the ad. We like the idea of using the slogan "HURT AT WORK?" in English and Spanish "HERIDO EN EL TRABAJO?";

We want minimal writing on the billboard. Our telephone number should be included. The ad should say "Millions Recovered for our clients" It should also say "Attorney Advertisement" in small font in a discrete place. We would like use colors that match/coordinate the colors of our logo and/or picture but it is not required. The design should communicate serious/professional tone with a hint of modern/vibrant attorneys.

Once we have something to work with we will work with the designer for adjustments.

All people injured at work

Law Firm

Requirements
Must have
• Must have HURT AT WORK and HERIDO EN EL TRABAJO (Spanish) OR another similar catchphrase
• Must have "Millions recovered for our clients"
• Must have telephone number (718) 555-0193
• Must have website "tkbriefhall.com"
• Must have in small font "Attorney Advertisement"

```html
<!DOCTYPE html>
<html lang="en">
<head>
<meta charset="utf-8">
<title>Torres &amp; Kline — Hurt at Work Billboard</title>
<link rel="stylesheet" href="https://fonts.googleapis.com/css2?family=Roboto+Condensed:wght@400;700;800&family=Roboto:wght@400&display=swap">
<style>
  :root {
    --stage: #5f5f5f;
    --paper: #efebe2;
    --paper-light: #f6f3ec;
    --ink: #0d0d0d;
    --gold: #8b7548;
    --red: #c41e30;
    --navy: #1f2c57;
    --caption: #cfcfcf;
  }
  * { margin: 0; padding: 0; box-sizing: border-box; }
  html, body { width: 1200px; height: 1200px; overflow: hidden; }
  body { background: var(--stage); position: relative; font-family: "Roboto", Arial, sans-serif; }

  .billboard {
    position: absolute; left: 226px; top: 114px; width: 760px; height: 950px;
    background: radial-gradient(ellipse at 60% 40%, var(--paper-light), var(--paper) 70%);
  }
  .billboard > * { position: absolute; white-space: nowrap; line-height: 1; }

  .brand {
    left: 64px; top: 66px; height: 36px;
    display: flex; align-items: center; gap: 10px;
    font-family: "Roboto Condensed", Arial, sans-serif; font-weight: 700;
    font-size: 26px; color: var(--gold); letter-spacing: 1px;
  }
  .brand-mark { width: 14px; height: 14px; background: var(--gold); }

  .headline {
    left: 108px; top: 117px;
    font-family: "Roboto Condensed", Arial, sans-serif;
    font-size: 85px; font-weight: 800; color: var(--ink); letter-spacing: -1px;
  }
  .headline-es {
    left: 108px; top: 195px;
    font-family: "Roboto Condensed", Arial, sans-serif;
    font-size: 56px; font-weight: 700; color: var(--gold); letter-spacing: -1.5px;
  }
  .claim-big {
    left: 206px; top: 254px;
    font-family: "Roboto Condensed", Arial, sans-serif;
    font-size: 92px; font-weight: 800; color: var(--red); letter-spacing: -2px;
  }
  .claim-mid {
    left: 206px; top: 340px;
    font-family: "Roboto Condensed", Arial, sans-serif;
    font-size: 74px; font-weight: 800; color: var(--red); letter-spacing: -1px;
  }
  .claim-small {
    left: 206px; top: 410px;
    font-family: "Roboto Condensed", Arial, sans-serif;
    font-size: 48px; font-weight: 400; color: var(--ink);
  }
  .website {
    right: 202px; top: 456px;
    display: flex; align-items: center; gap: 5px;
    font-size: 20px; color: var(--ink);
  }

  .portrait-area {
    left: 64px; top: 490px; width: 632px; height: 394px;
    background: linear-gradient(to bottom, rgba(239,235,226,0) 0%, #cdb8a6 35%, #b7998a 55%, var(--navy) 72%, var(--navy) 100%);
  }
  .disclaimer { left: 64px; top: 896px; font-size: 13px; color: var(--ink); }
  .phone {
    right: 62px; top: 890px;
    display: flex; align-items: center; gap: 4px;
    font-size: 29px; color: var(--ink);
  }
  .size-note {
    position: absolute; left: 0; width: 1206px; top: 1087px; text-align: center;
    font-family: "Roboto Condensed", Arial, sans-serif; font-size: 13px; color: var(--caption);
  }
</style>
</head>
<body>
  <main class="billboard">
    <div class="brand"><span class="brand-mark"></span>TORRES &amp; KLINE</div>

    <h1 class="headline">HURT AT WORK?</h1>
    <p class="headline-es">HERIDO EN EL TRABAJO?</p>

    <p class="claim-big">MILLIONS</p>
    <p class="claim-mid">RECOVERED</p>
    <p class="claim-small">FOR OUR CLIENTS</p>

    <div class="website">
      <svg width="18" height="18" viewBox="0 0 20 20" aria-hidden="true">
        <circle cx="10" cy="10" r="9" fill="var(--ink)"/>
        <g stroke="var(--paper)" stroke-width="1.2" fill="none">
          <ellipse cx="10" cy="10" rx="4" ry="9"/>
          <line x1="1" y1="10" x2="19" y2="10"/>
          <line x1="2.5" y1="5.5" x2="17.5" y2="5.5"/>
          <line x1="2.5" y1="14.5" x2="17.5" y2="14.5"/>
        </g>
      </svg>
      tkbriefhall.com
    </div>

    <div class="portrait-area" role="img" aria-label="Photo of the two attorneys in navy suits, one with a red tie and one with a blue tie"></div>

    <p class="disclaimer">ATTORNEY ADVERTISEMENT</p>
    <div class="phone">
      <svg width="26" height="26" viewBox="0 0 24 24" aria-hidden="true">
        <path fill="var(--ink)" d="M20 15.5c-1.2 0-2.4-.2-3.6-.6-.3-.1-.7 0-1 .2l-2.2 2.2c-2.8-1.4-5.1-3.8-6.6-6.6l2.2-2.2c.3-.3.4-.7.2-1-.3-1.1-.5-2.3-.5-3.5 0-.6-.4-1-1-1H4c-.5 0-1 .4-1 1 0 9.4 7.6 17 17 17 .6 0 1-.4 1-1v-3.5c0-.6-.4-1-1-1z" transform="scale(-1,1) translate(-24,0)"/>
      </svg>
      (718) 555-0193
    </div>
  </main>

  <p class="size-note">DESIGN SIZE : 8 FEET BY 10 FEET</p>
</body>
</html>
```